Postcard: Open Sky Circle

Text for front: HOW TO CHANGE THE WORLD IN ONE [note: the word "one" should be underlined] STEPHint: It's up to you...[Note: add arrow or something to indicate "turn over"]Text for back: You're going to spend your entire life with someone you can never get away from. (Guess who?) Wouldn't you rather that person #OpenSkyCircle than judgmental or critical? BE the change you want to see! Visit www.OpenSkyCircle-hub.example for daily Dawn Pebbles and community. PLEASE JOIN US![Note: add logo to left half of back side]Font preference for text: Josefin sans

Target Market(s)

People who would be attracted to Corvane church - teravian perennist message. It's spiritual without being overtly religious, so the target market is probably early 30s and up but ideally won't turn off Millennials (folks under 30). It should attract attention of people who are open-minded and committed to progressive social change, tired of an atmosphere of hate-mongering and divisiveness.

Requirements
Nice to have
• It would be nice to convey a sense of challenge - there is an idea of "dawn pebbles" so something related to fire/sparks is appropriate. This is meant to evoke a deeper, divine love more than a sense of romantic love. This love is more fierce than fluffy! Yet it calls us to be our best selves.
Should not have
• Please avoid excessive pink - just the logo is enough, as this design needs to appeal to men as well as women.

```html
<!DOCTYPE html>
<html lang="en">
<head>
<meta charset="utf-8">
<title>Open Sky Circle Postcard</title>
<link rel="stylesheet" href="https://fonts.googleapis.com/css2?family=Josefin+Sans:wght@400;600;700&family=Playfair+Display:ital@1&display=swap">
<style>
  :root {
    --page: #ffffff;
    --ink: #3f3f42;
    --ink-soft: #1f1f22;
    --pink: #f24fcf;
    --aqua-edge: #c9f7f7;
    --aqua-mid: #e7fbfb;
    --arrow-blue: #3aaef0;
    --arrow-light: #45c8e8;
    --globe-teal: #3fc9c0;
    --globe-pale: #d2f1f0;
    --logo-pink: #f03fbf;
    --logo-bg: #f7f7f7;
    --crop: #222;
  }
  * { margin: 0; padding: 0; box-sizing: border-box; }
  html, body { width: 1200px; height: 1000px; overflow: hidden; background: var(--page); }
  .canvas { position: relative; width: 1200px; height: 1000px; }

  .crop { position: absolute; background: var(--crop); }
  .crop.v { width: 1px; height: 25px; }
  .crop.h { height: 1px; width: 25px; }

  .card {
    position: absolute; left: 297px; top: 55px; width: 605px; height: 888px;
    overflow: hidden;
    background: radial-gradient(ellipse 62% 58% at 50% 50%, #ffffff 35%, var(--aqua-mid) 70%, var(--aqua-edge) 100%);
    font-family: "Josefin Sans", sans-serif;
    color: var(--ink);
  }

  .headline { position: absolute; left: 0; top: 88px; width: 100%; text-align: center; }
  .headline-top { font-weight: 600; font-size: 42px; letter-spacing: -0.5px; line-height: 1; }
  .headline-world {
    position: relative; height: 92px; margin-top: -4px;
    font-weight: 700; font-size: 104px; line-height: 1; color: var(--pink);
    display: flex; justify-content: center; align-items: flex-start;
  }
  .headline-world .letters { display: block; margin-top: 4px; }
  .globe-o { position: relative; width: 56px; height: 92px; margin: 0 2px; }
  .globe-o .the {
    position: absolute; top: 0; left: 50%; transform: translateX(-50%);
    font-size: 16px; font-weight: 600; color: var(--ink); letter-spacing: 2px;
  }
  .globe-o .globe {
    position: absolute; bottom: 4px; left: 0; width: 56px; height: 56px; border-radius: 50%;
    background: radial-gradient(circle at 35% 35%, #a6eee6, var(--globe-teal) 70%, #2aa99f);
  }
  .headline-bottom { font-weight: 600; font-size: 30px; line-height: 1; margin-top: 2px; }
  .headline-bottom u { text-decoration-thickness: 2px; text-underline-offset: 4px; }

  .hint {
    position: absolute; left: 138px; top: 294px; width: 100px; text-align: center;
    font-family: "Playfair Display", serif; font-style: italic;
    font-size: 25px; line-height: 30px; color: var(--ink);
  }
  .turn-arrow { position: absolute; left: 258px; top: 263px; }

  .logo-panel {
    position: absolute; left: 65px; top: 462px; width: 233px; height: 223px;
    background: var(--logo-bg);
    display: flex; flex-direction: column; align-items: center; justify-content: center; gap: 16px;
  }
  .logo-mark { width: 90px; height: 90px; border-radius: 50%; background: var(--logo-pink); }
  .logo-name { font-weight: 600; font-size: 22px; color: var(--logo-pink); letter-spacing: 0.5px; }

  .message {
    position: absolute; left: 308px; top: 478px; width: 240px;
    font-size: 16.5px; line-height: 22px; color: var(--ink-soft);
  }
  .message p { margin-bottom: 8px; }

  .earth {
    position: absolute; left: 75px; top: 697px; width: 454px; height: 454px; border-radius: 50%;
    background: radial-gradient(circle at 50% 40%, #f1fcfb, var(--globe-pale) 70%, #b9e9e6);
    opacity: 0.85;
  }

  .invite {
    position: absolute; left: 0; top: 740px; width: 100%; text-align: center;
    font-size: 17px; line-height: 23px; color: var(--ink-soft);
  }
  .invite strong { font-weight: 600; }
  .invite .rule { width: 290px; margin: 8px auto 10px; border-top: 1px dotted #777; }
  .invite .join {
    font-family: "Playfair Display", serif; font-style: italic;
    font-size: 27px; letter-spacing: 1px; line-height: 1;
  }
</style>
</head>
<body>
<div class="canvas">
  <div class="crop v" style="left:314px;top:30px"></div>
  <div class="crop v" style="left:885px;top:30px"></div>
  <div class="crop v" style="left:314px;top:943px"></div>
  <div class="crop v" style="left:885px;top:943px"></div>
  <div class="crop h" style="left:272px;top:71px"></div>
  <div class="crop h" style="left:902px;top:71px"></div>
  <div class="crop h" style="left:272px;top:927px"></div>
  <div class="crop h" style="left:902px;top:927px"></div>

  <div class="card">
    <div class="earth" role="img" aria-label="Faint illustration of the Earth rising from the bottom edge"></div>

    <div class="headline">
      <div class="headline-top">HOW TO CHANGE</div>
      <div class="headline-world">
        <span class="letters">W</span>
        <span class="globe-o">
          <span class="the">THE</span>
          <span class="globe" role="img" aria-label="Small globe illustration standing in for the letter O"></span>
        </span>
        <span class="letters">RLD</span>
      </div>
      <div class="headline-bottom">IN <u>ONE</u> STEP</div>
    </div>

    <div class="hint">IT’S<br>UP TO<br>YOU…</div>

    <svg class="turn-arrow" width="200" height="150" viewBox="0 0 200 150" aria-hidden="true">
      <path d="M10,2 C4,62 58,86 138,76" fill="none" stroke="var(--arrow-blue)" stroke-width="36"/>
      <path d="M12,6 C14,50 60,66 136,62" fill="none" stroke="var(--arrow-light)" stroke-width="14"/>
      <polygon points="122,28 196,84 124,142" fill="var(--arrow-blue)"/>
    </svg>

    <div class="logo-panel">
      <div class="logo-mark"></div>
      <div class="logo-name">Open Sky Circle</div>
    </div>

    <div class="message">
      <p>You're going to spend your entire life with someone you can never get away from.</p>
      <p>(Guess who?)</p>
      <p>Wouldn't you rather that person #OpenSkyCircle than judgemental or critical?</p>
      <p>BE the change you want to see!</p>
    </div>

    <div class="invite">
      <div>Visit <strong>www.OpenSkyCircle-hub.example</strong></div>
      <div>for daily Dawn Pebbles and community.</div>
      <div class="rule"></div>
      <div class="join">PLEASE JOIN US!</div>
    </div>
  </div>
</div>
</body>
</html>
```